Custom Header Designs - Automotive Parts - Alternator & Starter

We need 8 Header/Hero designs that will be used on our website. We are a company based in Montreal Canada and we re-manufacture Alternators and Starters for all types of vehicles. We offer a premium product and we are looking for premium designs that reflect the look of our packaging and the look of our website. Essentially we specialize in the sale and manufacture of two specific parts that go on all types of vehicles, Alternators and Starters. All text on these designs need to be editable as we will need to translate them to French once we get the source files.
Here are some websites of our competitors so you can draw some inspiration and see what our industry/business is all about:
https://www.qelvorparts.com/
https://www.zentrihaul.com/
Article that describes a remanufactured product, https://www.wombrixo.com/articles/starters-and-alternators-reman-vs-new.html
Our packaging is modern, sleek and professional. Our website is a B2B E-Commerce Site as well as an info site to promote our products. It is clean and minimal but we want the header/hero designs to help it stand out. Our main colors are blue and gray (as seen in our logo), but you can use whatever you like to compliment these colors.
Our packaging design was done on PixelTroupe, here is the link to that project so that you can see the packaging look and use any of the info that is from that project.
https://jobs.pixeltroupe.ca/job/5829463
The 8 Header/Hero designs will be used in the following areas, I have included a brief description of what we are looking for:
1 - Homepage Header/Hero image - This will be the homepage hero image therefore it should summarize the info described below. We offer premium quality re-manufactured alternators and starters. We are a wholesaler/distributor that services major auto-part stores with these quality products.
2 - General Product Header/Hero image - This image will be used as a header where the customer can learn general info about our products and any custom work we can do. This page will have a section where you can click to learn more about our individual product lines (links to product specific pages mentioned below) and a description of the custom work we can perform. We offer a two year manufacturers warranty.
3 - Alternator Product Header/Hero image - This image will be used to showcase our Alternator Product Line. Its purpose is to promote and advertise our premium re-manufactured alternators. This page will provide detailed info about our alternator re-manufacturing process and describe why our alternators are great.
4 - Starter Product Header/Hero image - This image will be used to showcase our Starter Product Line. Its purpose is to promote and advertise our premium re-manufactured starters. This page will provide detailed info about our starter re-manufacturing process and describe why our starters are great.
5 - General Header/Hero Image - This image will be used in most of our standard pages like our terms and conditions, privacy policy, warranty policy, our company page, etc. It needs to relate to the industry but be general enough so that we could use it in multiple areas
6 - Online Ordering Header image - This image will be used in our B2B area to introduce our customers to the Online Ordering system, its purpose is to advertise and explain some of the features of the Online Ordering system.
7 - B/O Re-Manufacture & Return Header Image - This image will be used in our B2B area to explain and advertise to our customers how our Backorder/R&R process works on our website. Essentially if we do not have the remanufactured part in stock but we have the core you could put the product on Backorder and we will remanufacture it in a few hours. If for any reason (rare vehicle, old vehicle, etc.) we do not have the core we will R&R (Remanufacture and Return) the customers core for them.
8 - Bulk Ordering Form Header Image - This image will be used in our B2B area to explain and advertise to our customers how our Bulk Ordering Form works on our website.
These hero/header images will be going on a Plankly/TillNest website and I am suggesting these images have a size of 1600 x 500, but we will take any other suggestions from the designers as you are the experts.
I have included a zip file that includes images of various elements that will help you in the design process.
Target Market(s)
Educate consumers about our products and attract auto supply chains to become distributors of our products.
Industry/Entity Type
Automotive Part

```html
<!DOCTYPE html>
<html lang="en">
<head>
<meta charset="UTF-8">
<title>Ampravo – Alternators &amp; Starters</title>
<link href="https://fonts.googleapis.com/css2?family=Roboto:wght@700;900&family=Baloo+2:wght@400;500;600&display=swap" rel="stylesheet">
<style>
  :root {
    --brand-blue: #1d3f89;
    --brand-blue-deep: #16326f;
    --charcoal: #2b2c2f;
    --charcoal-dark: #1c1d20;
    --white: #ffffff;
    --ring-gray: #b9bcc4;
    --logo-top: #ffffff;
    --logo-bottom: #a9b6d6;
  }
  * { margin: 0; padding: 0; box-sizing: border-box; }
  html, body { width: 1200px; height: 375px; overflow: hidden; background: var(--charcoal-dark); }
  .hero {
    position: relative;
    width: 1200px;
    height: 375px;
    overflow: hidden;
    background: radial-gradient(ellipse at 45% 45%, #3a3b3f 0%, var(--charcoal) 45%, var(--charcoal-dark) 100%);
  }
  .hero-shapes { position: absolute; inset: 0; }
  .brand-name {
    position: absolute;
    left: 118px; top: 115px;
    width: 222px;
    display: flex; align-items: center; justify-content: center; gap: 8px;
    font-family: "Roboto", sans-serif;
    font-weight: 900;
    font-size: 34px;
    color: var(--brand-blue);
  }
  .brand-dot { width: 18px; height: 18px; border-radius: 50%; background: var(--brand-blue); }
  .headline {
    position: absolute;
    left: 377px; top: 44px; width: 300px;
    text-align: center;
    font-family: "Roboto", sans-serif;
    font-weight: 900;
    font-size: 36px;
    line-height: 36.5px;
    color: var(--white);
    letter-spacing: 0.3px;
  }
  .intro {
    position: absolute;
    left: 377px; top: 168px; width: 300px;
    text-align: center;
    font-family: "Baloo 2", sans-serif;
    font-weight: 400;
    font-size: 13.5px;
    line-height: 22.5px;
    color: var(--white);
    letter-spacing: 0.4px;
  }
  .buy-button {
    position: absolute;
    left: 466px; top: 310px;
    width: 111px; height: 34px;
    border: 2px solid var(--white);
    border-radius: 7px;
    display: flex; align-items: center; justify-content: center;
    font-family: "Baloo 2", sans-serif;
    font-size: 17px;
    color: var(--white);
    text-decoration: none;
    padding-top: 2px;
  }
  .badge-text {
    position: absolute;
    left: 1017px; top: 40px; width: 86px;
    text-align: center;
    font-family: "Roboto", sans-serif;
    font-weight: 700;
    color: var(--white);
  }
  .badge-text .big { display: block; font-size: 20px; line-height: 22px; }
  .badge-text .small { display: block; font-size: 10.5px; line-height: 13px; font-weight: 700; }
  .call-line {
    position: absolute;
    left: 1181px; top: 160px;
    transform-origin: 0 0;
    transform: translateX(10px) rotate(90deg);
    white-space: nowrap;
    font-family: "Roboto", sans-serif;
    font-size: 14px;
    color: var(--white);
    letter-spacing: 0.5px;
    display: flex; align-items: center; gap: 6px;
  }
  .call-line strong { font-weight: 900; letter-spacing: 1.2px; }
  .phone-icon { width: 13px; height: 13px; transform: rotate(-90deg); }
</style>
</head>
<body>
<main class="hero">
  <svg class="hero-shapes" width="1200" height="375" viewBox="0 0 1200 375" aria-hidden="false">
    <defs>
      <linearGradient id="logoFill" x1="0" y1="0" x2="0" y2="1">
        <stop offset="0" stop-color="var(--logo-top)"/>
        <stop offset="0.5" stop-color="#eef1f8"/>
        <stop offset="1" stop-color="var(--logo-bottom)"/>
      </linearGradient>
      <radialGradient id="productFill" cx="0.55" cy="0.5" r="0.55">
        <stop offset="0" stop-color="#dfe4ee"/>
        <stop offset="0.6" stop-color="#b9c2d4"/>
        <stop offset="1" stop-color="#ffffff"/>
      </radialGradient>
    </defs>

    <!-- top-left brand band -->
    <path class="band-top-left" d="M0 0 H420 C400 30 380 40 340 60 C300 80 270 95 200 125 C130 155 80 190 0 215 Z" fill="var(--brand-blue)"/>
    <!-- right brand band -->
    <path class="band-right" d="M1165 0 H1200 V375 H1150 C1150 330 1130 300 1130 250 C1130 200 1120 160 1120 110 C1120 70 1150 60 1160 30 Z" fill="var(--brand-blue)"/>
    <!-- product backdrop -->
    <circle cx="948" cy="240" r="198" fill="var(--brand-blue)"/>
    <path d="M730 240 A218 218 0 0 1 1100 80" fill="none" stroke="var(--brand-blue)" stroke-width="1.5" opacity="0.8"/>
    <path d="M745 250 A205 205 0 0 1 1060 60" fill="none" stroke="var(--brand-blue)" stroke-width="1" opacity="0.6"/>

    <!-- logo rings -->
    <circle cx="225" cy="135" r="137" fill="none" stroke="var(--ring-gray)" stroke-width="1" opacity="0.8"/>
    <circle class="logo-disc" cx="229" cy="135" r="111" fill="url(#logoFill)"/>
    <circle cx="330" cy="42" r="17" fill="none" stroke="var(--white)" stroke-width="3.5"/>
    <circle cx="172" cy="262" r="17" fill="none" stroke="var(--brand-blue)" stroke-width="3.5"/>

    <!-- product image area -->
    <circle cx="934" cy="218" r="178" fill="url(#productFill)" role="img" aria-label="Photo of a remanufactured alternator"/>

    <!-- quality badge -->
    <circle cx="1060" cy="64" r="45" fill="var(--white)"/>
    <circle cx="1060" cy="64" r="40" fill="var(--brand-blue)"/>

    <!-- social circles -->
    <g class="social" fill="var(--brand-blue)">
      <circle cx="660" cy="358" r="10.5"/>
      <circle cx="690" cy="358" r="10.5"/>
      <circle cx="720" cy="358" r="10.5"/>
      <circle cx="750" cy="358" r="10.5"/>
    </g>
  </svg>

  <div class="brand-name"><span class="brand-dot"></span>Ampravo</div>

  <h1 class="headline">ALTERNATORS<br>&amp;<br>STARTERS</h1>
  <p class="intro">We offer premium quality re-manufactured alternators and starters. We are a wholesaler/distributor that services major auto-part stores with these quality products.</p>
  <a class="buy-button" href="#">Buy Now</a>

  <div class="badge-text"><span class="big">100%</span><span class="small">Factory<br>Tested</span></div>

  <div class="call-line">
    <svg class="phone-icon" viewBox="0 0 24 24"><path fill="#fff" d="M6.6 10.8a15.1 15.1 0 0 0 6.6 6.6l2.2-2.2c.3-.3.7-.4 1-.2 1.1.4 2.3.6 3.6.6.6 0 1 .4 1 1V20c0 .6-.4 1-1 1A17 17 0 0 1 3 4c0-.6.4-1 1-1h3.5c.6 0 1 .4 1 1 0 1.3.2 2.5.6 3.6.1.3 0 .7-.2 1z"/></svg>
    <span>CallToday: <strong>514-555-0187</strong></span>
  </div>
</main>
</body>
</html>
```